Business Card Design

We need a business card designed for our new company. Prefer a black card with white logo & writing.

Contact Information for Business Card

Dale Pickett, address: 7-4417 Larchmere Avenue, Abbotsford, BC, V3K 2R9, Office Phone: 604-555-0172, Cell: 604-555-0138, Email: dale@kelsoncoatworks.ca

Colors

Designer to choose only greyscale colors for use in the design.

```html
<!DOCTYPE html>
<html lang="en">
<head>
<meta charset="utf-8">
<title>Kelson Coatworks – Business Card</title>
<link href="https://fonts.googleapis.com/css2?family=Poppins:wght@400;600;700&display=swap" rel="stylesheet">
<style>
  :root {
    --backdrop: #1c1c1c;
    --card-black: #181514;
    --card-grey: #474544;
    --stripe-grey: #8a8a8a;
    --front-top: #5a5856;
    --front-bottom: #1a1716;
    --white: #ffffff;
  }
  * { margin: 0; padding: 0; box-sizing: border-box; }
  html, body { width: 1200px; height: 1015px; overflow: hidden; }
  body {
    background: radial-gradient(ellipse at 50% 40%, #2c2c2c 0%, var(--backdrop) 60%, #0c0c0c 100%);
    font-family: "Poppins", sans-serif;
    color: var(--white);
    position: relative;
  }
  .card {
    position: absolute;
    width: 640px;
    height: 366px;
    border-radius: 4px;
    overflow: hidden;
    box-shadow: 0 18px 40px rgba(0,0,0,0.6);
  }
  .card-front {
    left: 90px; top: 80px;
    background: linear-gradient(160deg, var(--front-top) 0%, #2a2726 40%, var(--front-bottom) 100%);
    display: flex; align-items: center; justify-content: center;
  }
  .card-back { left: 470px; top: 540px; background: var(--card-black); }
  .card-back .shapes { position: absolute; inset: 0; }
  .wordmark {
    display: flex; align-items: center; gap: 14px;
    font-weight: 700; font-size: 38px; letter-spacing: 1px;
    text-transform: uppercase; line-height: 1;
  }
  .wordmark .mark-square {
    width: 26px; height: 26px; border: 3px solid var(--white);
  }
  .card-back .wordmark {
    position: absolute; right: 40px; top: 90px; font-size: 28px;
  }
  .contact {
    position: absolute; left: 40px; bottom: 38px;
    font-size: 15px; line-height: 1.35;
  }
  .contact .name {
    font-weight: 700; font-size: 22px; text-transform: uppercase;
    margin-bottom: 14px; letter-spacing: 0.5px;
  }
  .contact .row { display: flex; align-items: center; gap: 8px; }
  .contact .row svg { width: 14px; height: 14px; flex: none; }
  .contact .address { margin-top: 22px; }
</style>
</head>
<body>
  <div class="card card-front">
    <div class="wordmark"><span class="mark-square"></span>Kelson Coatworks</div>
  </div>

  <div class="card card-back">
    <svg class="shapes" viewBox="0 0 640 366" preserveAspectRatio="none">
      <polygon points="0,110 205,110 440,366 0,366" fill="var(--card-grey)"/>
      <polygon points="360,250 395,250 445,366 420,366" fill="var(--stripe-grey)"/>
    </svg>
    <div class="wordmark"><span class="mark-square"></span>Kelson Coatworks</div>
    <div class="contact">
      <div class="name">Dale Pickett</div>
      <div class="row">
        <svg viewBox="0 0 24 24" fill="none" stroke="#fff" stroke-width="2"><path d="M5 3h4l2 5-3 2a12 12 0 0 0 6 6l2-3 5 2v4a2 2 0 0 1-2 2A17 17 0 0 1 3 5a2 2 0 0 1 2-2z"/></svg>
        604-555-0172
      </div>
      <div class="row">
        <svg viewBox="0 0 24 24" fill="none" stroke="#fff" stroke-width="2"><rect x="6" y="2" width="12" height="20" rx="2"/><line x1="11" y1="18" x2="13" y2="18"/></svg>
        604-555-0138
      </div>
      <div class="row">
        <svg viewBox="0 0 24 24" fill="none" stroke="#fff" stroke-width="2"><rect x="2" y="5" width="20" height="14"/><path d="M2 5l10 8 10-8"/></svg>
        dale@kelsoncoatworks.ca
      </div>
      <div class="address">7-4417 Larchmere Avenue,<br>Abbotsford, BC, V3K 2R9</div>
    </div>
  </div>
</body>
</html>
```